Werbebrief
Zielgruppe
Unsere Zielgruppe sind Geschäftsführer junger Unternehmen.
Hallo,
Wir benötigen einen "Werbebrief". Es ist jedoch weniger ein Brief, als viel mehr eine etwas größerer "Werbekarte" (diese soll 105 x 210mm groß sein).
Auf der Vorderseite soll folgender Text stehen:
Für Unternehmen, die gerne expandieren möchten
Auf der Rückseite soll folgender Link stehen:
www.tolvek-werk.de/Expandieren
Darunter soll folgendes stehen:
Ihr persönlicher Code: ABC123
Wichtig ist, dass wir den Code individuell ändern können, da jeder einen anderen Code bekommt.
Unser Logo und Corporate Farbe habe ich hochgeladen. Das Design sollte auf jeden Fall zu unserer Webseite passen (www.tolvek-werk.de)
Wir freuen uns auf Ihre Vorschläge.

```html
<!DOCTYPE html>
<html lang="de">
<head>
<meta charset="utf-8">
<title>Tolvek Werk – Werbekarte</title>
<link rel="stylesheet" href="https://fonts.googleapis.com/css2?family=Source+Sans+3:wght@400&display=swap">
<style>
  :root {
    --page-bg: #e8e5e0;
    --card-blue-light: #2655a0;
    --card-blue: #214c93;
    --card-blue-dark: #1b4283;
    --card-text: #ffffff;
    --code-field: #ffffff;
    --code-field-shade: #e6e8ee;
  }
  html, body {
    margin: 0;
    padding: 0;
    width: 1200px;
    height: 1200px;
    overflow: hidden;
    background: var(--page-bg);
  }
  .sheet {
    position: relative;
    width: 1200px;
    height: 1200px;
    font-family: "Source Sans 3", "Segoe UI", sans-serif;
    color: var(--card-text);
  }
  .card {
    position: absolute;
    left: 100px;
    width: 1000px;
    height: 500px;
    background: linear-gradient(165deg, var(--card-blue-light) 0%, var(--card-blue) 50%, var(--card-blue-dark) 100%);
    box-shadow: 0 6px 18px rgba(0, 0, 0, 0.25);
    overflow: hidden;
  }
  .card--front { top: 60px; }
  .card--back { top: 640px; }

  .brand {
    position: absolute;
    top: 32px;
    right: 40px;
    display: flex;
    align-items: center;
    gap: 14px;
    font-size: 41px;
    line-height: 1;
    letter-spacing: 0.2px;
  }
  .brand__dot {
    width: 22px;
    height: 22px;
    border-radius: 50%;
    background: var(--card-text);
  }

  .headline {
    position: absolute;
    top: 205px;
    left: 152px;
    width: 668px;
    margin: 0;
    font-weight: 400;
    font-size: 42px;
    line-height: 66px;
  }
  .headline__line { display: block; }
  .headline__line--second { text-align: right; }

  .landing-url {
    position: absolute;
    top: 195px;
    left: 59px;
    margin: 0;
    font-size: 42px;
    line-height: 50px;
  }
  .personal-code {
    position: absolute;
    top: 260px;
    right: 48px;
    margin: 0;
    display: flex;
    align-items: center;
    gap: 8px;
    font-size: 42px;
    line-height: 50px;
  }
  .personal-code__field {
    display: inline-block;
    width: 240px;
    height: 40px;
    background: linear-gradient(180deg, var(--code-field) 0%, var(--code-field-shade) 100%);
  }
</style>
</head>
<body>
<main class="sheet">
  <section class="card card--front" aria-label="Vorderseite">
    <div class="brand"><span class="brand__dot"></span><span class="brand__name">Tolvek Werk</span></div>
    <h1 class="headline">
      <span class="headline__line">Für Unternehmen, die gerne</span>
      <span class="headline__line headline__line--second">expandieren möchten</span>
    </h1>
  </section>

  <section class="card card--back" aria-label="Rückseite">
    <div class="brand"><span class="brand__dot"></span><span class="brand__name">Tolvek Werk</span></div>
    <p class="landing-url">www.tolvek-werk.de/Expandieren</p>
    <p class="personal-code">Ihr persönlicher Code: <span class="personal-code__field" aria-label="Feld für den persönlichen Code"></span></p>
  </section>
</main>
</body>
</html>
```